Stationary for mobile ultrasound company
Business card, letter head and envelope design
Stationary for mobile ultrasound company - Imaging
Modern
Lorna Pettibone, RDMS, ARRT
Owner/Operator
5718 N. Quarry Hollow Ln. Tullowmere, Nordale 83791
lumenscanhealth@corvilmail.net
www. plinthory.com
Please add tag line under logo: Improving ultrasound in a convenient and personal way.
Appointment time and date spaces. Please try logo as is and with black backgrounds on front of card

```html
<!DOCTYPE html>
<html lang="en">
<head>
<meta charset="utf-8">
<title>Lumenscan Mobile Imaging – Business Card</title>
<link href="https://fonts.googleapis.com/css2?family=Montserrat:wght@400;600;800&display=swap" rel="stylesheet">
<style>
  :root{
    --stage:#eef0f3;
    --card:#ffffff;
    --purple:#8a2f9e;
    --purple-deep:#6d1f84;
    --teal:#1f7f94;
    --ink:#4a4a52;
    --muted:#8a8d94;
    --line:#d9dbe0;
  }
  *{box-sizing:border-box;margin:0;padding:0}
  html,body{width:1200px;height:980px;overflow:hidden}
  body{background:var(--stage);font-family:"Montserrat",sans-serif;position:relative}
  .card{
    position:absolute;width:760px;height:434px;background:var(--card);
    border-radius:26px;overflow:hidden;
    box-shadow:0 2px 6px rgba(0,0,0,.12);
  }
  .card-back{left:400px;top:40px}
  .card-front{left:40px;top:506px}

  .brand{display:flex;align-items:center;gap:14px}
  .brand-mark{width:30px;height:30px;border-radius:50%;background:var(--teal);flex:none}
  .brand-name{color:var(--purple);font-weight:800;font-size:34px;letter-spacing:.5px;line-height:1;white-space:nowrap}

  .card-back .brand{position:absolute;right:64px;top:196px}
  .back-web{
    position:absolute;left:48px;top:90px;color:var(--muted);
    font-size:14px;letter-spacing:4px;transform:rotate(-8deg);transform-origin:left top;
    white-space:nowrap;
  }

  .card-front .brand{position:absolute;left:74px;top:60px}
  .contact{position:absolute;left:74px;top:128px;list-style:none}
  .contact li{display:flex;align-items:center;gap:10px;font-size:13px;color:var(--ink);line-height:24px;white-space:nowrap}
  .contact .dot{width:14px;height:14px;border-radius:50%;background:var(--teal);flex:none;display:flex;align-items:center;justify-content:center}
  .contact .dot svg{width:8px;height:8px}

  .swoosh{position:absolute;left:0;top:0;width:760px;height:434px}
  .signature{position:absolute;right:44px;bottom:34px;text-align:right;color:#fff}
  .signature .person{font-weight:600;font-size:17px}
  .signature .role{font-size:13px;margin-top:4px;opacity:.9}
</style>
</head>
<body>

<section class="card card-back" aria-label="Business card back">
  <p class="back-web">www. plinthory.com</p>
  <div class="brand">
    <span class="brand-mark"></span>
    <span class="brand-name">Lumenscan Mobile Imaging</span>
  </div>
</section>

<section class="card card-front" aria-label="Business card front">
  <svg class="swoosh" viewBox="0 0 760 434" aria-hidden="true">
    <defs>
      <linearGradient id="bandFill" x1="0" y1="0" x2="1" y2="0">
        <stop offset="0" stop-color="#a040b5"/>
        <stop offset="1" stop-color="#6d1f84"/>
      </linearGradient>
    </defs>
    <path d="M0 318 C 230 290, 480 305, 760 210" fill="none" stroke="#d9dbe0" stroke-width="10"/>
    <path d="M0 300 C 240 268, 500 292, 760 226 L760 250 C 500 318, 240 296, 0 326 Z" fill="#1f7f94"/>
    <path d="M0 340 C 250 305, 510 322, 760 258 L760 434 L0 434 Z" fill="url(#bandFill)"/>
  </svg>

  <div class="brand">
    <span class="brand-mark"></span>
    <span class="brand-name">Lumenscan Mobile Imaging</span>
  </div>

  <ul class="contact">
    <li><span class="dot"><svg viewBox="0 0 10 10"><path d="M5 1a3 3 0 0 1 3 3c0 2-3 5-3 5S2 6 2 4a3 3 0 0 1 3-3z" fill="#fff"/></svg></span>5718 N. Quarry Hollow Ln.</li>
    <li><span class="dot"><svg viewBox="0 0 10 10"><circle cx="5" cy="5" r="2" fill="#fff"/></svg></span>Tullowmere, Nordale 83791</li>
    <li><span class="dot"><svg viewBox="0 0 10 10"><path d="M2 1h2l1 2-1 1a5 5 0 0 0 2 2l1-1 2 1v2c-4 0-7-3-7-7z" fill="#fff"/></svg></span>(208) 555-0142</li>
    <li><span class="dot"><svg viewBox="0 0 10 10"><path d="M2 1h2l1 2-1 1a5 5 0 0 0 2 2l1-1 2 1v2c-4 0-7-3-7-7z" fill="#fff"/></svg></span>(208) 555-0187</li>
    <li><span class="dot"><svg viewBox="0 0 10 10"><path d="M1 2h8v6H1z M1 2l4 3 4-3" fill="none" stroke="#fff" stroke-width="1.2"/></svg></span>lumenscanhealth@corvilmail.net</li>
    <li><span class="dot"><svg viewBox="0 0 10 10"><circle cx="5" cy="5" r="3.5" fill="none" stroke="#fff" stroke-width="1.2"/></svg></span>www. plinthory.com</li>
  </ul>

  <div class="signature">
    <p class="person">Lorna Pettibone, RDMS, ARRT</p>
    <p class="role">Owner/Operator</p>
  </div>
</section>

</body>
</html>
```